Velmora Design

Looking for Velmora banner and square design:
Velmora Banner
W:1600 px H:400 px
Square
120x120

Logo attached.

Description: Data-Driven stock market portfolio management using quantitative analysis.

```html
<!DOCTYPE html>
<html lang="en">
<head>
<meta charset="utf-8">
<title>Velmora – Banner and Square</title>
<link rel="stylesheet" href="https://fonts.googleapis.com/css2?family=Montserrat:wght@600&family=Roboto:ital,wght@0,400;0,500;1,700&display=swap">
<style>
  :root {
    --stage: #141414;
    --paper: #ffffff;
    --brand-blue: #0a78be;
    --brand-navy: #1b5a8c;
    --headline-blue: #0b72bb;
    --screen-frame: #d6dce3;
    --screen-bg: #f1f4f7;
    --card: #ffffff;
    --line: #e3e7ec;
    --muted: #9aa4ae;
    --ink: #3c4650;
    --bar-light: #d5dbe2;
    --table-head: #1d3f66;
  }
  html, body {
    margin: 0;
    padding: 0;
    width: 1200px;
    height: 733px;
    overflow: hidden;
    background: var(--stage);
  }
  .canvas { position: relative; width: 1200px; height: 733px; }
  .defs { position: absolute; width: 0; height: 0; }
  .banner-slot { position: absolute; overflow: hidden; background: var(--paper); }
  .banner-slot--wide { left: 71px; top: 79px; width: 1058px; height: 265px; }
  .banner-slot--compact { left: 354px; top: 469px; width: 775px; height: 194px; }
  .banner { position: absolute; left: 0; top: 0; width: 1058px; height: 265px; transform-origin: 0 0; }
  .banner-slot--compact .banner { transform: scale(0.7335); }
  .banner__blob { position: absolute; left: 0; top: 0; }
  .banner__screen { position: absolute; left: 72px; top: 120px; width: 365px; height: 146px; }
  .dash-text { font-family: "Roboto", sans-serif; font-weight: 400; fill: var(--ink); }
  .dash-text--title { font-weight: 500; font-size: 4px; }
  .dash-text--small { font-size: 2.6px; fill: var(--muted); }
  .dash-text--nav { font-size: 2.8px; fill: var(--muted); }
  .dash-text--active { font-size: 2.8px; fill: var(--paper); font-weight: 500; }
  .dash-text--brand { font-family: "Montserrat", sans-serif; font-weight: 600; font-size: 4px; fill: var(--brand-navy); }
  .dash-text--head { font-size: 2.6px; fill: var(--paper); font-weight: 500; }
  .wordmark { position: absolute; left: 72px; top: 42px; display: flex; align-items: center; gap: 14px; }
  .wordmark__dot { width: 48px; height: 48px; border-radius: 50%; background: var(--brand-blue); }
  .wordmark__name {
    font-family: "Montserrat", sans-serif; font-weight: 600; font-size: 40px;
    letter-spacing: 1px; color: var(--brand-navy);
  }
  .headline {
    position: absolute; margin: 0;
    font-family: "Roboto", sans-serif; font-style: italic; font-weight: 700;
    font-size: 55px; line-height: 1; color: var(--headline-blue); white-space: nowrap;
  }
  .headline__line { position: absolute; display: block; }
  .headline__line--first { left: 545px; top: 86px; }
  .headline__line--second { left: 530px; top: 141px; }
  .square {
    position: absolute; background: var(--brand-blue);
    display: flex; align-items: center; justify-content: center;
    font-family: "Montserrat", sans-serif; font-weight: 600; color: var(--paper);
  }
  .square--small { left: 553px; top: 297px; width: 94px; height: 94px; border-radius: 15px; font-size: 17px; }
  .square--large { left: 71px; top: 463px; width: 200px; height: 200px; border-radius: 26px; font-size: 36px; }
</style>
</head>
<body>
<svg class="defs" aria-hidden="true">
  <symbol id="dashboard" viewBox="0 0 365 146">
    <rect x="0" y="0" width="365" height="146" rx="2" fill="var(--screen-frame)"/>
    <rect x="15" y="6" width="333" height="140" fill="var(--screen-bg)"/>
    <!-- top bar -->
    <rect x="15" y="6" width="333" height="18" fill="var(--card)"/>
    <rect x="71" y="11" width="64" height="8" rx="4" fill="var(--screen-bg)"/>
    <text class="dash-text dash-text--small" x="75" y="16">Search</text>
    <circle cx="131" cy="15" r="1.6" fill="none" stroke="var(--brand-blue)" stroke-width="0.6"/>
    <circle cx="275" cy="15" r="2" fill="none" stroke="var(--brand-blue)" stroke-width="0.6"/>
    <circle cx="289" cy="15" r="2" fill="none" stroke="var(--muted)" stroke-width="0.6"/>
    <circle cx="310" cy="15" r="3" fill="var(--bar-light)"/>
    <rect x="315" y="13" width="14" height="1.6" fill="var(--ink)"/>
    <rect x="315" y="16" width="10" height="1.2" fill="var(--muted)"/>
    <!-- sidebar -->
    <rect x="15" y="6" width="49" height="140" fill="var(--card)"/>
    <circle cx="21" cy="15" r="3" fill="var(--brand-blue)"/>
    <text class="dash-text dash-text--brand" x="26" y="16.5">VELMORA</text>
    <rect x="16" y="34" width="44" height="8" rx="4" fill="var(--brand-blue)"/>
    <text class="dash-text dash-text--active" x="23" y="39">Conservative</text>
    <text class="dash-text dash-text--nav" x="23" y="52">Growth</text>
    <text class="dash-text dash-text--nav" x="23" y="65">Whale</text>
    <text class="dash-text dash-text--nav" x="23" y="78">Member Tools</text>
    <text class="dash-text dash-text--nav" x="23" y="91">Membership</text>
    <rect x="18" y="49.5" width="3" height="3" fill="var(--bar-light)"/>
    <rect x="18" y="62.5" width="3" height="3" fill="var(--bar-light)"/>
    <rect x="18" y="75.5" width="3" height="3" fill="var(--bar-light)"/>
    <rect x="18" y="88.5" width="3" height="3" fill="var(--bar-light)"/>
    <!-- total return card -->
    <rect x="71" y="31" width="186" height="89" rx="2" fill="var(--card)"/>
    <text class="dash-text dash-text--title" x="76" y="39">Total Return %</text>
    <circle cx="161" cy="37.8" r="1.3" fill="var(--brand-blue)"/>
    <text class="dash-text dash-text--small" x="164" y="39">Portfolio 60/40</text>
    <circle cx="201" cy="37.8" r="1.3" fill="var(--bar-light)"/>
    <text class="dash-text dash-text--small" x="204" y="39">Benchmark</text>
    <g stroke="var(--line)" stroke-width="0.4">
      <line x1="90" y1="53" x2="250" y2="53"/>
      <line x1="90" y1="65" x2="250" y2="65"/>
      <line x1="90" y1="77" x2="250" y2="77"/>
      <line x1="90" y1="89" x2="250" y2="89"/>
      <line x1="90" y1="101" x2="250" y2="101"/>
      <line x1="90" y1="111" x2="250" y2="111"/>
    </g>
    <rect x="102" y="106" width="8" height="5" fill="var(--brand-blue)"/>
    <rect x="111" y="107" width="8" height="4" fill="var(--bar-light)"/>
    <rect x="144" y="106" width="8" height="5" fill="var(--brand-blue)"/>
    <rect x="153" y="106.5" width="8" height="4.5" fill="var(--bar-light)"/>
    <rect x="185" y="89" width="8" height="22" fill="var(--brand-blue)"/>
    <rect x="194" y="99" width="8" height="12" fill="var(--bar-light)"/>
    <rect x="226" y="66" width="8" height="45" fill="var(--brand-blue)"/>
    <rect x="235" y="93" width="8" height="18" fill="var(--bar-light)"/>
    <text class="dash-text dash-text--small" x="106" y="116">YTD</text>
    <text class="dash-text dash-text--small" x="149" y="116">1yr</text>
    <text class="dash-text dash-text--small" x="190" y="116">3yr</text>
    <text class="dash-text dash-text--small" x="231" y="116">5yr</text>
    <!-- growth rate card -->
    <rect x="261" y="31" width="82" height="89" rx="2" fill="var(--card)"/>
    <text class="dash-text dash-text--title" x="265" y="39">Annual Growth Rate</text>
    <line x1="283" y1="46" x2="283" y2="110" stroke="var(--line)" stroke-width="0.5"/>
    <text class="dash-text dash-text--small" x="266" y="55">1yr</text>
    <rect x="283" y="50" width="37" height="5" fill="var(--brand-blue)"/>
    <rect x="283" y="56" width="28" height="5" fill="var(--bar-light)"/>
    <text class="dash-text dash-text--small" x="266" y="75">3yr</text>
    <rect x="283" y="70" width="36" height="5" fill="var(--brand-blue)"/>
    <rect x="283" y="76" width="18" height="5" fill="var(--bar-light)"/>
    <text class="dash-text dash-text--small" x="266" y="95">5yr</text>
    <rect x="283" y="90" width="37" height="5" fill="var(--brand-blue)"/>
    <rect x="283" y="96" width="19" height="5" fill="var(--bar-light)"/>
    <!-- yearly return card -->
    <rect x="71" y="124" width="186" height="22" rx="2" fill="var(--card)"/>
    <text class="dash-text dash-text--title" x="76" y="131">Yearly Total Return %</text>
    <rect x="230" y="139" width="4" height="7" fill="var(--brand-blue)"/>
    <!-- allocation card -->
    <rect x="261" y="124" width="82" height="22" rx="2" fill="var(--card)"/>
    <text class="dash-text dash-text--title" x="265" y="131">Current Allocation</text>
    <rect x="265" y="134" width="74" height="5" fill="var(--table-head)"/>
    <text class="dash-text dash-text--head" x="267" y="137.8">TICKER</text>
    <text class="dash-text dash-text--head" x="318" y="137.8">% ALLOCATION</text>
  </symbol>
</svg>
<main class="canvas">

  <section class="banner-slot banner-slot--wide">
    <div class="banner">
      <svg class="banner__blob" width="1058" height="265" viewBox="0 0 1058 265" aria-hidden="true">
        <path d="M16 265 C10 190 40 150 100 140 C200 120 330 100 395 102 C405 104 405 118 400 125 C420 160 460 210 479 265 Z" fill="var(--brand-blue)"/>
      </svg>
      <svg class="banner__screen" viewBox="0 0 365 146" role="img" aria-label="Portfolio dashboard with return charts">
        <use href="#dashboard"/>
      </svg>
      <div class="wordmark">
        <span class="wordmark__dot"></span>
        <span class="wordmark__name">VELMORA</span>
      </div>
      <h1 class="headline">
        <span class="headline__line headline__line--first">RULES-BASED</span>
        <span class="headline__line headline__line--second">STOCK PORTFOLIO</span>
      </h1>
    </div>
  </section>

  <div class="square square--small">Velmora</div>

  <div class="square square--large">Velmora</div>

  <section class="banner-slot banner-slot--compact">
    <div class="banner">
      <svg class="banner__blob" width="1058" height="265" viewBox="0 0 1058 265" aria-hidden="true">
        <path d="M16 265 C10 190 40 150 100 140 C200 120 330 100 395 102 C405 104 405 118 400 125 C420 160 460 210 479 265 Z" fill="var(--brand-blue)"/>
      </svg>
      <svg class="banner__screen" viewBox="0 0 365 146" role="img" aria-label="Portfolio dashboard with return charts">
        <use href="#dashboard"/>
      </svg>
      <div class="wordmark">
        <span class="wordmark__dot"></span>
        <span class="wordmark__name">VELMORA</span>
      </div>
      <h2 class="headline">
        <span class="headline__line headline__line--first">RULES-BASED</span>
        <span class="headline__line headline__line--second">STOCK PORTFOLIO</span>
      </h2>
    </div>
  </section>

</main>
</body>
</html>
```